eBook Cover Design (German language)

Hello everyone,

at the moment I'm writing a book in German language and I'm looking for a cover for my e book.

Book title:
Mut zum eigenen Kompass! (=courage for one's own compass)
Nimm den Anlauf jetzt! (=take the run-up now)

Author: Tarek Ostrowski

Book summary:
The book is about how students get better at school and how their future life depends on their decisions

Target audience:
students in the age between 15 and 20 years old.

I tried to draw some suggestions and here are two options for you..

OPTION 1:
at the left side beginning a small mountain wich is called "Schulzeit" (=Schooltime)
At this mountain is 1 happy and 1 unhappy student, who are climbing to the top.
From the top of the mountain there is a bridge to the bigger mountain wich is called "Berufsleben" (=Working life). On this bigger mountain there is a happy student wich is rising his thumb.
Between this two mountains is a student wich is unhappy and crying. The bridge in the pdf data is not a must have.

OPTION 2:
1 student in the middle of the cover wo is looking at 1 small mountain wich is called "Schulzeit" (=Schooltime) and a bigger mountain behind wich is called "Berufsleben" (=Working life)

left side of the cover: bad weather, bad mountain, bad way and a crying student
right side of cover: good weather, nice mountain and on the top of the bigger mountain is a very happy student wich is raising his thumb.

OPTION 3:
Here you should only represent the mountains and the flag more realistically.
Please concentrate only on the picture. We can add the individual headings afterwards and adjust them as desired.

If you need any further information, you can contact me and I will answer as soon as possible.

Best regards, Tarek Ostrowski

```html
<!DOCTYPE html>
<html lang="de">
<head>
<meta charset="utf-8">
<title>Mut zum eigenen Kompass! – Buchcover</title>
<link rel="stylesheet" href="https://fonts.googleapis.com/css2?family=Old+Standard+TT:wght@400;700&display=swap">
<style>
  :root {
    --page-bg: #7f9ee2;
    --ink: #161616;
    --accent-blue: #2f6fb0;
    --label-ink: #f2f2f2;
    --chart-line: #d8dde3;
    --sky-top: #f4eed3;
    --sky-mid: #c7d5e3;
    --sky-low: #93abc6;
    --haze: #6f8299;
    --ridge: #151515;
    --ground: #040404;
  }
  * { margin: 0; padding: 0; box-sizing: border-box; }
  html, body {
    width: 1200px;
    height: 856px;
    overflow: hidden;
    background: var(--page-bg);
  }
  .book-cover {
    position: absolute;
    left: 352px;
    top: 48px;
    width: 495px;
    height: 760px;
    overflow: hidden;
    font-family: "Old Standard TT", "Times New Roman", serif;
  }
  .cover-photo {
    position: absolute;
    inset: 0;
    background: linear-gradient(168deg,
      var(--sky-top) 0%,
      var(--sky-mid) 24%,
      var(--sky-low) 42%,
      var(--haze) 54%,
      var(--ridge) 66%,
      var(--ground) 100%);
  }
  .growth-chart {
    position: absolute;
    inset: 0;
    width: 495px;
    height: 760px;
  }
  .cover-title {
    position: absolute;
    left: 0;
    right: 0;
    top: 30px;
    text-align: center;
    color: var(--ink);
    font-weight: 700;
    font-size: 60px;
    line-height: 96px;
    letter-spacing: -1px;
  }
  .cover-title .accent { color: var(--accent-blue); }
  .cover-subtitle {
    position: absolute;
    left: 0;
    right: 0;
    top: 246px;
    text-align: center;
    color: var(--ink);
    font-weight: 700;
    font-size: 34px;
  }
  .cover-subtitle .accent { color: var(--accent-blue); }
  .stage-label {
    position: absolute;
    color: var(--label-ink);
    font-size: 25px;
    font-weight: 400;
  }
  .stage-label--work { left: 315px; top: 412px; }
  .stage-label--school { left: 47px; top: 576px; }
  .cover-author {
    position: absolute;
    left: 0;
    right: 0;
    top: 712px;
    text-align: center;
    color: var(--label-ink);
    font-size: 32px;
    letter-spacing: 1px;
  }
</style>
</head>
<body>
  <main class="book-cover">
    <div class="cover-photo" role="img" aria-label="Photo: misty mountain range at sunrise with dark slope silhouettes and climbers ascending toward a summit"></div>

    <svg class="growth-chart" viewBox="0 0 495 760" aria-hidden="true">
      <path d="M20 464 L156 464 L275 418 Q380 360 448 250" fill="none" stroke="var(--chart-line)" stroke-width="2.5"/>
      <path d="M436 258 L450 246 L450 265" fill="none" stroke="var(--chart-line)" stroke-width="2.5"/>
    </svg>

    <h1 class="cover-title">Mut zum <span class="accent">eigenen</span><br>Kompass!</h1>
    <p class="cover-subtitle"><span class="accent">Nimm</span> den Anlauf jetzt!</p>

    <span class="stage-label stage-label--work">Berufsleben</span>
    <span class="stage-label stage-label--school">Schulzeit</span>

    <p class="cover-author">Tarek Ostrowski</p>
  </main>
</body>
</html>
```